Accident Law Firm Billboard Bold Easy to See Car Accidents

We need a billboard design that can catch attention in a very crowed Car Accident lawyer market. We wish to feature the phone number (652) 318-4470 as the focus of the Bill Board. We are trying to get the phone number recognized and remembered by drivers. The law firm name is not as crucial to remember.
Basically, It's CAR ACCIDENT? Then (652) 318-4470. We are not married to any specific color scheme but it has to POP and catch attention.
So the Crucial elements are as follows:
1. Phone number (652) 318-4470
2. Words CAR ACCIDENT?
3. Firm Logo in lower portion or where appropriate. Firm Logo to be provided
4. We may want to try a Day Glow orange color, with White and Black added. An example of the color scheme shall be provided.
5. Possible "Catch Phrase" to be used, "It's Time Call 9"
Target Market(s)
Orlando Florida Car Accident victims
Industry/Entity Type
Law Firm
Requirements
Must have
- Easy to see phone number (652) 318-4470
- Catch attention
Nice to have
- I would like to have the sign visible in bright sunlight and it not too hard to immediately know what phone number is for
Should not have
- too many words
- No bold enough
- confusing fonts
- Unclear fonts

```html
<!DOCTYPE html>
<html lang="en">
<head>
<meta charset="utf-8">
<title>Marravelli Law Firm – Car Accident Billboard</title>
<link rel="stylesheet" href="https://fonts.googleapis.com/css2?family=Roboto+Condensed:wght@700;800&display=swap">
<style>
  :root {
    --page-bg: #ecebe8;
    --sign-white: #ffffff;
    --ink-black: #1a1a1a;
    --ink-grey: #5b5b5b;
    --day-glow: #f5420f;
    --day-glow-light: #ff6b2c;
    --band-grey: #5e5e5e;
  }
  html, body {
    margin: 0;
    padding: 0;
    width: 752px;
    height: 1200px;
    overflow: hidden;
    background: var(--page-bg);
  }
  .canvas {
    position: relative;
    width: 752px;
    height: 1200px;
    display: flex;
    align-items: center;
    justify-content: center;
  }
  .billboard {
    width: 712px;
    height: 475px;
    display: block;
    box-shadow: 0 8px 24px rgba(0, 0, 0, 0.22);
    background: var(--sign-white);
  }
  .firm-name {
    font-family: "Roboto Condensed", sans-serif;
    font-weight: 700;
    fill: var(--ink-black);
  }
  .firm-square { fill: var(--ink-black); }
  .headline {
    font-family: "Roboto Condensed", sans-serif;
    font-weight: 800;
  }
  .headline-grey { fill: var(--ink-grey); }
  .headline-orange { fill: var(--day-glow); }
  .phone {
    font-family: "Roboto Condensed", sans-serif;
    font-weight: 800;
    fill: var(--sign-white);
    stroke: #3a1205;
    stroke-width: 3px;
    paint-order: stroke;
  }
  .catch-phrase {
    font-family: "Roboto Condensed", sans-serif;
    font-weight: 700;
    fill: var(--sign-white);
  }
</style>
</head>
<body>
<main class="canvas">
  <svg class="billboard" viewBox="0 0 720 480" role="img" aria-label="Marravelli Law Firm P.C. billboard: Car Accident? Call (652) 318-4470. It's time call 9">
    <defs>
      <linearGradient id="glow-banner" x1="0" y1="0" x2="1" y2="0">
        <stop offset="0" stop-color="#f5420f"/>
        <stop offset="1" stop-color="#ff6b2c"/>
      </linearGradient>
      <linearGradient id="glow-tip" x1="0" y1="0" x2="0" y2="1">
        <stop offset="0" stop-color="#ff6b2c"/>
        <stop offset="1" stop-color="#f5420f"/>
      </linearGradient>
    </defs>

    <rect class="sign-face" x="0" y="0" width="720" height="480" fill="var(--sign-white)"/>

    <g class="firm-mark">
      <rect class="firm-square" x="218" y="44" width="24" height="24"/>
      <text class="firm-name" x="254" y="67" font-size="32">MARRAVELLI LAW FIRM P.C.</text>
    </g>

    <text class="headline" x="360" y="168" text-anchor="middle" font-size="76">
      <tspan class="headline-grey">CAR </tspan><tspan class="headline-orange">ACCIDENT?</tspan>
    </text>

    <g class="phone-banner">
      <polygon class="banner-tail" points="416,330 634,328 622,370 420,374" fill="var(--band-grey)"/>
      <polygon class="banner-tip" points="420,368 520,368 492,415" fill="url(#glow-tip)"/>
      <polygon class="banner-body" points="65,220 660,180 632,330 120,330" fill="url(#glow-banner)"/>
      <text class="phone" x="372" y="290" text-anchor="middle" font-size="66" textLength="480" lengthAdjust="spacingAndGlyphs">(652) 318-4470</text>
    </g>

    <g class="catch-band">
      <polygon class="catch-band-orange" points="0,416 282,416 246,480 0,480" fill="var(--day-glow)"/>
      <polygon class="catch-band-grey" points="282,416 720,416 720,480 246,480" fill="var(--band-grey)"/>
      <text class="catch-phrase" x="492" y="466" text-anchor="middle" font-size="48" textLength="346" lengthAdjust="spacingAndGlyphs">IT'S TIME CALL 9</text>
    </g>
  </svg>
</main>
</body>
</html>
```